Business Card Design Project

Looking for a simple and stylish business card. We are an Advertising Company. The card Must feature the company logo (attached) and also this info.
p: 0461528390
e: sales@jh-promo.com.au
w: www.jh-promo.com.au
We Advertise mainly using TV screens featured in restaurants and cafe. See website for more about the business.
Not really looking for a plain background, but at the same time do not want to much happening in the Background. I am not really to fussy though with the design or the colour scheme, and I am leaving the creativity part up to you creative designers.
Business

```html
<!DOCTYPE html>
<html lang="en">
<head>
<meta charset="utf-8">
<title>JH Promo — Business Card</title>
<link rel="stylesheet" href="https://fonts.googleapis.com/css2?family=Montserrat:ital,wght@0,300;0,400;0,700;1,700&display=swap">
<style>
  :root {
    --page-bg: #ffffff;
    --card-bg: #ffffff;
    --brand-blue: #1e4a96;
    --band-blue: #3a439a;
    --brand-pink: #e5195a;
    --pink-light: #ef4e60;
    --pattern-tint: #e3f3fa;
  }
  * { box-sizing: border-box; margin: 0; padding: 0; }
  html, body {
    width: 1200px;
    height: 1000px;
    overflow: hidden;
    background: var(--page-bg);
    font-family: "Montserrat", Arial, sans-serif;
  }
  .business-card {
    position: absolute;
    left: 222px;
    top: 273px;
    width: 756px;
    height: 432px;
    background: var(--card-bg);
    overflow: hidden;
    box-shadow: 4px 5px 8px rgba(0, 0, 0, 0.28);
  }
  .background-texture {
    position: absolute;
    left: 160px;
    top: 0;
    width: 596px;
    height: 360px;
    background: radial-gradient(ellipse at 85% 20%, var(--pattern-tint) 0%, rgba(227, 243, 250, 0.5) 40%, rgba(227, 243, 250, 0) 75%);
  }
  .company-name {
    position: absolute;
    left: 37px;
    top: 62px;
    font-size: 68px;
    font-weight: 400;
    letter-spacing: 2px;
    line-height: 1;
    color: var(--brand-blue);
  }
  .contact-list {
    position: absolute;
    left: 38px;
    top: 178px;
    list-style: none;
    font-size: 21px;
    line-height: 33px;
    color: var(--brand-blue);
  }
  .contact-list .label { font-weight: 400; }
  .contact-list .value { font-weight: 700; }
  .person {
    position: absolute;
    right: 38px;
    top: 244px;
    text-align: right;
    color: var(--brand-pink);
    font-size: 23px;
    line-height: 33px;
  }
  .person .role { font-weight: 700; font-style: italic; }
  .person .name { font-weight: 400; }
  .footer-band {
    position: absolute;
    left: 0;
    bottom: 0;
    width: 756px;
    height: 90px;
    background: linear-gradient(180deg, var(--band-blue) 0%, var(--pink-light) 55%, var(--brand-pink) 100%);
  }
</style>
</head>
<body>
  <div class="business-card">
    <div class="background-texture" role="img" aria-label="Faint light-blue pattern of small diamond stars"></div>

    <div class="company-name">JH PROMO</div>

    <ul class="contact-list">
      <li><span class="label">p: </span><span class="value">0461528390</span></li>
      <li><span class="label">e: </span><span class="value">sales@jh-promo.com.au</span></li>
      <li><span class="label">w: </span><span class="value">www.jh-promo.com.au</span></li>
    </ul>

    <div class="person">
      <div class="role">Managing Director</div>
      <div class="name">Mark Delaney</div>
    </div>

    <div class="footer-band" role="img" aria-label="Decorative blue and pink footer band"></div>
  </div>
</body>
</html>
```